https://dorvakel.com

We need a cool technology design for our Managed IT Services company. We are located in Coral Springs Florida. We provide all IT services and support for small to medium sized businesses. We would like to see designs that use our blue and white colors from our website.

```html
<!DOCTYPE html>
<html lang="en">
<head>
<meta charset="utf-8">
<title>Dorvakel Business Card</title>
<link rel="stylesheet" href="https://fonts.googleapis.com/css2?family=Roboto:wght@400;500;700&family=Roboto+Condensed:wght@500;700&display=swap">
<style>
  :root {
    --backdrop: #e9ebef;
    --navy: #13284b;
    --navy-deep: #0d1f3c;
    --sky: #2a9be0;
    --electric: #3fc3f5;
    --ink: #1b2640;
    --accent-blue: #3a63b0;
    --tile-light: #c9cfe8;
    --tile-mid: #7e8bc4;
    --tile-dark: #3d5690;
    --white: #ffffff;
  }
  * { box-sizing: border-box; margin: 0; padding: 0; }
  html, body { width: 1200px; height: 908px; overflow: hidden; }
  body {
    background: var(--backdrop);
    font-family: "Roboto", Arial, sans-serif;
    position: relative;
  }
  .card {
    position: absolute;
    width: 620px;
    height: 354px;
    border-radius: 22px;
    overflow: hidden;
    box-shadow: 0 10px 28px rgba(20, 30, 60, 0.18);
  }

  /* Front: services */
  .card-front {
    left: 90px; top: 80px;
    background: var(--navy);
  }
  .front-artwork {
    position: absolute;
    right: 0; top: 0;
    width: 380px; height: 100%;
    background:
      radial-gradient(circle at 62% 38%, rgba(255,255,255,0.85) 0%, rgba(120,210,255,0.55) 10%, rgba(42,155,224,0) 34%),
      radial-gradient(circle at 55% 45%, var(--electric) 0%, var(--sky) 35%, rgba(19,40,75,0) 75%),
      linear-gradient(90deg, var(--navy) 0%, #1c4f8e 40%, #2574c2 100%);
  }
  .front-logo {
    position: absolute;
    left: 40px; top: 56px;
    font-family: "Roboto", Arial, sans-serif;
    font-weight: 700;
    font-size: 44px;
    letter-spacing: 1px;
    color: var(--white);
  }
  .service-list {
    position: absolute;
    left: 44px; top: 130px;
    list-style: none;
    font-family: "Roboto Condensed", Arial, sans-serif;
    font-weight: 500;
    font-size: 19px;
    line-height: 24px;
    color: var(--white);
    text-transform: uppercase;
  }
  .service-list li { display: flex; align-items: center; }
  .service-list li::before {
    content: "";
    width: 8px; height: 8px;
    background: var(--white);
    margin-right: 14px;
    flex: none;
  }

  /* Back: contact */
  .card-back {
    left: 490px; top: 470px;
    background: var(--white);
  }
  .back-pattern {
    position: absolute;
    left: 0; top: 0;
    width: 260px; height: 100%;
    background:
      radial-gradient(ellipse at 10% 30%, var(--tile-dark) 0%, var(--tile-mid) 35%, var(--tile-light) 60%, rgba(255,255,255,0) 85%);
  }
  .back-logo {
    position: absolute;
    right: 44px; top: 46px;
    font-weight: 700;
    font-size: 46px;
    letter-spacing: 1px;
    color: var(--ink);
  }
  .contact-block {
    position: absolute;
    right: 44px; top: 120px;
    text-align: right;
    color: var(--ink);
  }
  .person-name {
    font-weight: 500;
    font-size: 23px;
    letter-spacing: 2.5px;
    text-transform: uppercase;
  }
  .person-title {
    font-size: 17px;
    letter-spacing: 2.5px;
    color: var(--accent-blue);
    text-transform: uppercase;
    margin-top: 2px;
  }
  .contact-lines {
    margin-top: 12px;
    font-size: 17px;
    line-height: 22px;
  }
  .address-lines {
    margin-top: 14px;
    font-size: 17px;
    line-height: 22px;
  }
</style>
</head>
<body>
  <section class="card card-front">
    <div class="front-artwork" role="img" aria-label="Glowing blue globe with network icons for people, settings and charts"></div>
    <div class="front-logo">DORVAKEL</div>
    <ul class="service-list">
      <li>Managed IT</li>
      <li>IT Data Services</li>
      <li>Security Services</li>
      <li>Software Services</li>
      <li>Hardware Services</li>
      <li>Business Services</li>
      <li>Cloud IT</li>
      <li>Industry Specific</li>
    </ul>
  </section>

  <section class="card card-back">
    <div class="back-pattern" role="img" aria-label="Mosaic of blue and lavender tiles curving outward like a sphere"></div>
    <div class="back-logo">DORVAKEL</div>
    <div class="contact-block">
      <div class="person-name">Marcus Delane-Ruiz</div>
      <div class="person-title">Chief Executive Officer</div>
      <div class="contact-lines">
        <div>(954) 555-0182</div>
        <div>yourname@dorvakel.com</div>
        <div>www.dorvakel.com</div>
      </div>
      <div class="address-lines">
        <div>2180 Harbor Palm Blvd #140</div>
        <div>Coral Springs, Florida 33065</div>
      </div>
    </div>
  </section>
</body>
</html>
```